tri-fold brochure design for psychology practice - all content provided

we are a psychology practice that specialises in diagnostic and educational assessments for children, adolescents and adults. We have an existing logo and I am attaching a word doc (tri-fold brochure) with the required content. I am also attaching our logo and other relevant content docs. The layout is only a sample and we are looking for someone to put this together into a consistent and better layout.

Target Market(s)

parents

Industry/Entity Type

education and health

Font styles to use
Other font styles liked:
• crimsonpro

Requirements
Must have
• our logo and the provided content

```html
<!DOCTYPE html>
<html lang="en">
<head>
<meta charset="utf-8">
<title>brightpath – tri-fold brochure</title>
<link href="https://fonts.googleapis.com/css2?family=Crimson+Pro:wght@400;600&family=Montserrat:wght@400;500;600;700&display=swap" rel="stylesheet">
<style>
  :root{
    --page:#ececec;
    --paper:#ffffff;
    --green:#4f7f2a;
    --green-deep:#3f6a1f;
    --green-light:#6a9a3c;
    --brown:#4a3521;
    --blue:#4f95d8;
    --teal:#4cc98c;
    --ink:#2b2b2b;
    --text:#3a3a3a;
    --tab-dark:#262626;
    --icon-circle:#3c5a24;
  }
  *{box-sizing:border-box;margin:0;padding:0}
  html,body{width:1200px;height:2400px;overflow:hidden;background:var(--page)}
  body{font-family:"Montserrat",Arial,sans-serif;color:var(--text);position:relative}

  .spread{position:absolute;left:0;width:1200px;height:929px;background:var(--paper);overflow:hidden;box-shadow:0 6px 24px rgba(0,0,0,.12)}
  .spread--outside{top:150px}
  .spread--inside{top:1240px}

  .photo{position:absolute}
  svg.layer{position:absolute;left:0;top:0}

  .brand{position:absolute;text-align:center;width:340px}
  .brand__name{display:inline-flex;align-items:center;gap:10px;font-family:"Crimson Pro",Georgia,serif;font-weight:600;font-size:44px;line-height:1;color:var(--ink)}
  .brand__dot{width:16px;height:16px;border-radius:50%;background:var(--green)}
  .brand__tag{font-family:"Crimson Pro",Georgia,serif;font-size:13px;color:var(--text);margin-top:4px}

  .process-card{position:absolute;left:54px;width:290px;height:172px}
  .process-card__frame{position:absolute;left:0;top:0;width:100%;height:120px;border-radius:10px}
  .process-card__title{position:relative;height:40px;display:flex;align-items:center;justify-content:center;gap:8px;color:#fff;font-weight:600;font-size:17px}
  .process-card__title svg{width:20px;height:20px}
  .process-card__body{position:absolute;left:8px;right:8px;top:40px;height:132px;background:#fff;border-radius:8px;box-shadow:0 2px 8px rgba(0,0,0,.18);display:flex;align-items:center;justify-content:center;text-align:center;padding:10px 22px;font-size:12.5px;line-height:1.2;color:var(--text)}
  .process-card__tab{position:absolute;left:50%;bottom:-20px;width:60px;height:20px;margin-left:-30px;clip-path:polygon(0 0,100% 0,100% 50%,50% 100%,0 50%)}
  .process-card--understand .process-card__frame,.process-card--understand .process-card__tab{background:var(--blue)}
  .process-card--identify .process-card__frame,.process-card--identify .process-card__tab{background:var(--teal)}
  .process-card--guide .process-card__frame,.process-card--guide .process-card__tab{background:var(--green-light)}

  .contact-list{position:absolute;left:400px;width:400px;top:600px;text-align:center;color:#fff;font-weight:600;font-size:14.5px}
  .contact{position:absolute;left:0;width:100%}
  .contact__icon{display:block;margin:0 auto 6px;width:26px;height:26px}

  .cover-heading{position:absolute;left:800px;width:400px;top:718px;text-align:center;color:#fff;font-weight:600;font-size:34px;line-height:39px;letter-spacing:.3px}
  .cover-rule{position:absolute;left:870px;width:260px;top:843px;height:1px;background:rgba(255,255,255,.6)}
  .cover-rule::after{content:"";position:absolute;left:105px;top:-2px;width:50px;height:4px;background:#fff;border-radius:2px}
  .web{position:absolute;width:400px;text-align:center;font-size:19px}
  .web--cover{left:800px;top:864px;color:#fff}
  .web--steps{left:800px;top:870px;color:var(--ink)}

  .deco-circle{position:absolute;border-radius:50%}

  .who{position:absolute;left:40px;top:300px;width:300px;color:#fff}
  .who__title{font-weight:700;font-size:21px;margin-bottom:12px}
  .who p{font-size:13.5px;line-height:1.22;margin-bottom:16px}

  .about{position:absolute;left:432px;top:145px;width:332px;font-size:13.5px;line-height:1.18;color:var(--text)}
  .about p{text-align:justify;margin-bottom:16px}
  .conditions{list-style:none;margin:-4px 0 12px}
  .conditions li{display:flex;align-items:center;gap:12px;font-weight:600;font-size:13px;color:var(--ink);height:23px}
  .conditions svg{width:15px;height:15px;flex:none}

  .step{position:absolute;left:844px;width:303px;height:150px}
  .step__frame{position:absolute;left:0;top:0;width:100%;height:96px;background:var(--green-light);border-radius:10px}
  .step__num{position:relative;height:38px;line-height:38px;text-align:center;color:#fff;font-weight:600;font-size:19px}
  .step__body{position:absolute;left:8px;right:8px;top:38px;height:94px;background:#fff;border-radius:8px;box-shadow:0 2px 8px rgba(0,0,0,.18);display:flex;align-items:center;justify-content:center;text-align:center;padding:8px 16px;font-size:12.5px;line-height:1.2}
  .step__tab{position:absolute;left:50%;top:132px;width:60px;height:22px;margin-left:-30px;background:var(--tab-dark);clip-path:polygon(0 0,100% 0,100% 55%,50% 100%,0 55%)}
</style>
</head>
<body>

<section class="spread spread--outside">
  <div class="photo" role="img" aria-label="Black and white photo of a young child playing with building blocks while a woman holds up drawings of smiling faces" style="left:0;top:600px;width:400px;height:329px;background:linear-gradient(180deg,#d6d6d6 0%,#9e9e9e 45%,#7a7a7a 100%)"></div>

  <div class="process-card process-card--understand" style="top:36px">
    <div class="process-card__frame"><div class="process-card__title">
      <svg viewBox="0 0 20 20" fill="none" stroke="#fff" stroke-width="1.6"><rect x="2" y="3" width="16" height="11" rx="1"/><path d="M7 18h6M10 14v4M6 10l3-3 2 2 3-3"/></svg>UNDERSTANDING</div></div>
    <div class="process-card__body">Assessment starts with listening first, and then asking the right questions in order to ensure that we are understanding your concerns and hearing your questions.</div>
    <div class="process-card__tab"></div>
  </div>

  <div class="process-card process-card--identify" style="top:238px">
    <div class="process-card__frame"><div class="process-card__title">
      <svg viewBox="0 0 20 20" fill="none" stroke="#fff" stroke-width="1.6"><circle cx="8" cy="8" r="5"/><path d="M12 12l6 6"/></svg>IDENTIFYING</div></div>
    <div class="process-card__body">It is then our job to use our diagnostic and assessment knowledge and skills to collect the right data in order to address your concerns and provide answers to your questions.</div>
    <div class="process-card__tab"></div>
  </div>

  <div class="process-card process-card--guide" style="top:444px">
    <div class="process-card__frame"><div class="process-card__title">
      <svg viewBox="0 0 20 20" fill="none" stroke="#fff" stroke-width="1.6"><rect x="3" y="2" width="14" height="16" rx="1"/><path d="M6 7h8M6 11h8M6 15h5"/></svg>GUIDING</div></div>
    <div class="process-card__body">This then enables us to provide you with recommendations for accessing support and interventions that arebased on current best practice and are suported by evidence.</div>
    <div class="process-card__tab"></div>
  </div>

  <div class="photo" role="img" aria-label="Photo of a woman and two young boys playing with stacking rings in a bright playroom" style="left:400px;top:170px;width:800px;height:500px;background:linear-gradient(90deg,#ffffff 0%,#eeece8 18%,#d9d2c8 45%,#c9d3de 70%,#e6e2dc 100%)"></div>

  <svg class="layer" style="left:400px" width="800" height="929" viewBox="0 0 800 929">
    <defs>
      <linearGradient id="coverGreen" x1="0" y1="0" x2="0" y2="1">
        <stop offset="0" stop-color="#3f6a1f"/><stop offset="1" stop-color="#5d8f30"/>
      </linearGradient>
    </defs>
    <path d="M0,688 C120,580 230,452 350,450 C460,448 520,582 620,592 C700,600 760,540 800,483 V929 H0Z" fill="var(--brown)"/>
    <path d="M0,708 C120,600 230,472 350,470 C460,468 520,602 620,612 C700,620 760,560 800,505 V929 H0Z" fill="url(#coverGreen)"/>
  </svg>

  <div class="brand" style="left:432px;top:90px">
    <div class="brand__name"><span class="brand__dot"></span>brightpath</div>
    <div class="brand__tag">diagnostic and educational assessments</div>
  </div>
  <div class="brand" style="left:827px;top:90px">
    <div class="brand__name"><span class="brand__dot"></span>brightpath</div>
    <div class="brand__tag">diagnostic and educational assessments</div>
  </div>

  <div class="contact-list">
    <div class="contact" style="top:0">
      <svg class="contact__icon" viewBox="0 0 26 26"><circle cx="13" cy="13" r="13" fill="var(--icon-circle)"/><path d="M9 7c1 0 2 2 2 3s-1 1-1 2 2 3 3 3 1-1 2-1 3 1 3 2-1 2-2 2c-4 0-9-5-9-9 0-1 1-2 2-2z" fill="#fff"/></svg>
      02 9000 4417
    </div>
    <div class="contact" style="top:65px">
      <svg class="contact__icon" viewBox="0 0 26 26"><circle cx="13" cy="13" r="13" fill="var(--icon-circle)"/><rect x="7" y="9" width="12" height="9" rx="1" fill="#fff"/><path d="M7 9l6 5 6-5" fill="none" stroke="var(--icon-circle)" stroke-width="1.2"/></svg>
      hello@brightpath.example
    </div>
    <div class="contact" style="top:132px;line-height:1.2">
      <svg class="contact__icon" viewBox="0 0 26 26"><circle cx="13" cy="13" r="13" fill="var(--icon-circle)"/><path d="M13 6a5 5 0 0 1 5 5c0 4-5 9-5 9s-5-5-5-9a5 5 0 0 1 5-5z" fill="#fff"/><circle cx="13" cy="11" r="2" fill="var(--icon-circle)"/></svg>
      12/48 Harbour View Rd, Seaview<br>NSW 2100
    </div>
    <div class="contact" style="top:233px">
      <svg class="contact__icon" viewBox="0 0 26 26"><circle cx="13" cy="13" r="13" fill="var(--icon-circle)"/><g fill="none" stroke="#fff" stroke-width="1.3"><circle cx="13" cy="13" r="6"/><ellipse cx="13" cy="13" rx="2.6" ry="6"/><path d="M7 13h12"/></g></svg>
      www.brightpath.example
    </div>
  </div>

  <div class="deco-circle" style="left:1111px;top:607px;width:54px;height:54px;background:var(--green-deep)"></div>

  <h1 class="cover-heading">UNDERSTANDING<br>IDENTIFYING<br>GUIDING</h1>
  <div class="cover-rule"></div>
  <div class="web web--cover">www.brightpath.example</div>
</section>

<section class="spread spread--inside">
  <svg class="layer" width="1200" height="929" viewBox="0 0 1200 929">
    <defs>
      <linearGradient id="insideGreen" x1="0" y1="0" x2="0" y2="1">
        <stop offset="0" stop-color="#4f7f2a"/><stop offset="1" stop-color="#3f6a1f"/>
      </linearGradient>
      <linearGradient id="topPhoto" x1="0" y1="0" x2="0" y2="1">
        <stop offset="0" stop-color="#8ba06f"/><stop offset=".6" stop-color="#5f8a3b"/><stop offset="1" stop-color="#4f7f2a" stop-opacity="0"/>
      </linearGradient>
      <linearGradient id="bottomPhoto" x1="0" y1="0" x2="1" y2="0">
        <stop offset="0" stop-color="#e4d8cc"/><stop offset=".5" stop-color="#f2ede6"/><stop offset="1" stop-color="#ffffff"/>
      </linearGradient>
      <linearGradient id="greyPhoto" x1="0" y1="0" x2="0" y2="1">
        <stop offset="0" stop-color="#ffffff"/><stop offset=".35" stop-color="#d8d8d8"/><stop offset="1" stop-color="#9a9a9a"/>
      </linearGradient>
    </defs>
    <path d="M0,0 H440 C380,150 360,350 366,575 C250,580 120,600 0,630 Z" fill="url(#insideGreen)"/>
    <path d="M440,0 H462 C402,150 380,350 380,575 L366,575 C360,350 380,150 440,0Z" fill="var(--green-light)"/>
    <g role="img" aria-label="Green tinted photo of two toddlers playing with a toy on the floor">
      <path d="M0,0 H436 C392,110 372,220 366,300 H0Z" fill="url(#topPhoto)"/>
    </g>
    <g role="img" aria-label="Photo of a smiling teacher with glasses helping a young boy write">
      <path d="M0,640 C140,600 280,580 385,585 C420,700 450,820 480,929 H0Z" fill="url(#bottomPhoto)"/>
    </g>
    <g role="img" aria-label="Black and white photo of a psychologist working with a young boy at a table">
      <path d="M500,929 C480,820 470,730 490,665 H830 V929Z" fill="url(#greyPhoto)"/>
    </g>
    <circle cx="346" cy="552" r="20" fill="#fff"/>
  </svg>

  <div class="who">
    <h2 class="who__title">WHO WE ARE</h2>
    <p>brightpath is a team with a passion for helping people to thrive.  We are a team of psychologists and teachers who have experience in both educational and clinical settings.</p>
    <p>We understand the challenges parents face in wanting what is best for their children, trying to understand how and where to access the most relevant information and support.</p>
  </div>

  <div class="brand" style="left:432px;top:55px">
    <div class="brand__name"><span class="brand__dot"></span>brightpath</div>
    <div class="brand__tag">diagnostic and educational assessments</div>
  </div>

  <div class="about">
    <p>We are passionate about wanting to help families navigate the diagnostic and assessment process.</p>
    <p>We believe that quality and comprehensive assessment needs to happen before intervention begins. We work collaboratively with other professionals to ensure that recommendations and supports put in place are appropriate and evidence-based while also meeting the needs of the individual.</p>
    <p>We are qualified to give formal diagnoses for mental health conditions and specific learning disorders. This includes:</p>
    <ul class="conditions">
      <li><svg viewBox="0 0 15 15"><circle cx="7.5" cy="7.5" r="7.5" fill="var(--green-deep)"/><path d="M4 7.8l2.3 2.2 4.7-4.7" fill="none" stroke="#fff" stroke-width="1.8"/></svg>Attention Deficit Hyperactivity Disorder</li>
      <li><svg viewBox="0 0 15 15"><circle cx="7.5" cy="7.5" r="7.5" fill="var(--green-deep)"/><path d="M4 7.8l2.3 2.2 4.7-4.7" fill="none" stroke="#fff" stroke-width="1.8"/></svg>Autism Spectrum Disorder</li>
      <li><svg viewBox="0 0 15 15"><circle cx="7.5" cy="7.5" r="7.5" fill="var(--green-deep)"/><path d="M4 7.8l2.3 2.2 4.7-4.7" fill="none" stroke="#fff" stroke-width="1.8"/></svg>Specific Learning Disorders</li>
      <li><svg viewBox="0 0 15 15"><circle cx="7.5" cy="7.5" r="7.5" fill="var(--green-deep)"/><path d="M4 7.8l2.3 2.2 4.7-4.7" fill="none" stroke="#fff" stroke-width="1.8"/></svg>Language disorders</li>
      <li><svg viewBox="0 0 15 15"><circle cx="7.5" cy="7.5" r="7.5" fill="var(--green-deep)"/><path d="M4 7.8l2.3 2.2 4.7-4.7" fill="none" stroke="#fff" stroke-width="1.8"/></svg>Anxiety Disorders</li>
      <li><svg viewBox="0 0 15 15"><circle cx="7.5" cy="7.5" r="7.5" fill="var(--green-deep)"/><path d="M4 7.8l2.3 2.2 4.7-4.7" fill="none" stroke="#fff" stroke-width="1.8"/></svg>Mood Disorders</li>
      <li><svg viewBox="0 0 15 15"><circle cx="7.5" cy="7.5" r="7.5" fill="var(--green-deep)"/><path d="M4 7.8l2.3 2.2 4.7-4.7" fill="none" stroke="#fff" stroke-width="1.8"/></svg>Communication Disorders</li>
    </ul>
    <p>We are passionate about collaborating with your school or workplace, supporting you in applying for financial support if available (such as NDIS funding), and to feel more informed and confident in your decisions.</p>
  </div>

  <div class="step" style="top:38px">
    <div class="step__frame"><div class="step__num">01</div></div>
    <div class="step__body">An initial face-to-face interview to discuss your concerns and understand the relevant background and details</div>
    <div class="step__tab"></div>
  </div>
  <div class="step" style="top:202px">
    <div class="step__frame"><div class="step__num">02</div></div>
    <div class="step__body">A formal assessment session during which relevant tests are completed. This can include IQ testing, Achievement testing, Memory testing, Personality profiling etc.</div>
    <div class="step__tab"></div>
  </div>
  <div class="step" style="top:367px">
    <div class="step__frame"><div class="step__num">03</div></div>
    <div class="step__body">Obtaining additional information through questionnaires, observation, contact with other professionals (such as teachers/tutors etc).</div>
    <div class="step__tab"></div>
  </div>
  <div class="step" style="top:537px">
    <div class="step__frame"><div class="step__num">04</div></div>
    <div class="step__body">A feedback session during which we provide you with a final draft of the report and discuss possible recommendations, collaborating about the next steps.</div>
    <div class="step__tab"></div>
  </div>
  <div class="step" style="top:704px">
    <div class="step__frame"><div class="step__num">05</div></div>
    <div class="step__body">A copy of the finalised report is provided and opportunity for discussion and engagement with teachers or other allied health is provided</div>
    <div class="step__tab"></div>
  </div>

  <div class="web web--steps">www.brightpath.example</div>
</section>

</body>
</html>
```